New name flyer

We have just changed our business name from kR Property group to Harbour Lantern. We want to distribute a flyer to the local community to inform them of the change. We are a realestate agency which focuses mainly on property management but also sales. We service from Brisbane to the Sunshine coast.

Target Market(s)

Local community

Industry/Entity Type

realestate

Requirements
Must have
• Details of name change
Nice to have
• Servicing area Brisbane and Sunshine Coast, no change in management or services we offer, and will continue pride ourselves on offering a high level of service, with the same team from the Gold to Sunshine Coast.
Should not have
• too much wording.

```html
<!DOCTYPE html>
<html lang="en">
<head>
<meta charset="utf-8">
<title>Harbour Lantern – New Name Flyer</title>
<link rel="stylesheet" href="https://fonts.googleapis.com/css2?family=Source+Sans+3:wght@400;600;700&display=swap">
<style>
  :root{
    --navy:#1c2d5e;
    --gold:#c9962f;
    --white:#ffffff;
    --ink:#3b3b3b;
    --backdrop:#e9e9ec;
    --sky:#4f86c6;
    --pool:#3fb6cf;
    --stone:#d9d6cf;
    --room:#c9ccd2;
    --bed:#5d6472;
  }
  *{box-sizing:border-box;margin:0;padding:0}
  html,body{width:1200px;height:800px;overflow:hidden}
  body{background:var(--backdrop);font-family:"Source Sans 3",Arial,sans-serif;position:relative}

  .flyer{position:absolute;left:330px;top:18px;width:540px;height:764px;background:var(--white);box-shadow:0 4px 14px rgba(0,0,0,.18);overflow:hidden}

  .masthead{height:131px;background:var(--navy);display:flex;justify-content:space-between;align-items:center;padding:0 20px 0 22px}
  .brand{display:flex;align-items:center;gap:10px;color:var(--white);font-weight:700;font-size:21px;line-height:1.05;letter-spacing:.5px;text-transform:uppercase}
  .brand-square{width:14px;height:14px;background:var(--white)}
  .masthead-note{text-align:right;color:var(--white);font-size:19px;line-height:1.3;text-transform:uppercase;font-weight:400}
  .masthead-note strong{color:var(--gold);font-weight:700;display:block}

  .gallery{position:absolute;top:153px;left:15px;width:510px;height:355px}
  .photo,.tile{position:absolute}
  .photo-hero{left:0;top:0;width:261px;height:355px;background:linear-gradient(180deg,var(--sky) 0%,#9cc3e6 35%,#f1f1ef 55%,var(--pool) 78%,#8a6a52 100%)}
  .tile{background:var(--navy);width:115px;height:114px}
  .col-a{left:271px}
  .col-b{left:395px}
  .row-1{top:0}
  .row-2{top:120px}
  .row-3{top:241px}
  .photo-kitchen{background:linear-gradient(180deg,#e9edf1 0%,#cfd6de 60%,#8d99a8 100%)}
  .photo-living{background:linear-gradient(180deg,#eeeeec 0%,var(--room) 60%,#7b7e84 100%)}
  .photo-bedroom{background:linear-gradient(180deg,#6f7480 0%,var(--bed) 50%,#9aa6c0 100%)}

  .announcement{position:absolute;top:540px;left:0;width:100%;text-align:center}
  .announcement h1{color:var(--navy);font-size:15.5px;font-weight:600;line-height:32px;text-transform:uppercase}
  .announcement h1 strong{font-weight:700}
  .divider{width:100px;height:1.5px;background:var(--gold);margin:8px auto 14px}
  .announcement p{color:var(--ink);font-size:12px;line-height:20.5px;width:440px;margin:0 auto}

  .contact-tab{position:absolute;left:0;top:709px;width:186px;height:28px}
  .contact-tab svg{position:absolute;inset:0}
  .contact-tab span{position:relative;color:var(--white);font-size:15px;line-height:28px;padding-left:22px}
  .contact-bar{position:absolute;left:0;top:737px;width:100%;height:27px;background:var(--navy);display:flex;align-items:center;justify-content:space-between;padding:0 24px;color:var(--white);font-size:11.5px;font-weight:600}
  .contact-item{display:flex;align-items:center;gap:5px}
  .contact-item svg{width:11px;height:11px}
</style>
</head>
<body>
  <main class="flyer">
    <header class="masthead">
      <div class="brand"><span class="brand-square"></span><span>Harbour<br>Lantern</span></div>
      <p class="masthead-note">We have just changed<br>our business name to<strong>Harbour Lantern</strong></p>
    </header>

    <section class="gallery">
      <div class="photo photo-hero" role="img" aria-label="Modern white two-storey home with swimming pool and garden"></div>
      <div class="tile col-a row-1"></div>
      <div class="photo tile col-b row-1 photo-kitchen" role="img" aria-label="Bright modern kitchen with island bench and pendant lights"></div>
      <div class="photo tile col-a row-2 photo-living" role="img" aria-label="Light living room with sofa and round coffee table"></div>
      <div class="tile col-b row-2"></div>
      <div class="tile col-a row-3"></div>
      <div class="photo tile col-b row-3 photo-bedroom" role="img" aria-label="Contemporary bedroom with blue bedding"></div>
    </section>

    <section class="announcement">
      <h1>We have just changed our business name<br>from <strong>kR Property group</strong> to <strong>Harbour Lantern</strong></h1>
      <div class="divider"></div>
      <p>Servicing area Brisbane and Sunshine Coast, no change in management or services we offer, and will continue pride ourselves on offering a high level of service, with the same team from the Gold to Sunshine Coast.</p>
    </section>

    <div class="contact-tab">
      <svg viewBox="0 0 186 28" preserveAspectRatio="none"><polygon points="0,0 176,0 186,28 0,28" fill="#c9962f"/></svg>
      <span>Contact Us</span>
    </div>
    <footer class="contact-bar">
      <span class="contact-item">
        <svg viewBox="0 0 12 12"><circle cx="6" cy="6" r="5.5" fill="none" stroke="#fff"/><rect x="3" y="4" width="6" height="4" fill="none" stroke="#fff" stroke-width=".8"/><polyline points="3,4 6,6.3 9,4" fill="none" stroke="#fff" stroke-width=".8"/></svg>
        admin@harbourlantern.com.au
      </span>
      <span class="contact-item">
        <svg viewBox="0 0 12 12"><circle cx="6" cy="6" r="5.5" fill="none" stroke="#fff"/><path d="M4 3.2l1 1.3-.6.8c.4.8 1 1.4 1.8 1.8l.8-.6 1.3 1-.6 1C5.6 8.4 3.6 6.4 3.5 4z" fill="#fff"/></svg>
        07 3000 2718
      </span>
      <span class="contact-item">
        <svg viewBox="0 0 12 12"><circle cx="6" cy="6" r="5.5" fill="none" stroke="#fff"/><circle cx="6" cy="6" r="3" fill="none" stroke="#fff" stroke-width=".8"/><line x1="3" y1="6" x2="9" y2="6" stroke="#fff" stroke-width=".8"/><ellipse cx="6" cy="6" rx="1.2" ry="3" fill="none" stroke="#fff" stroke-width=".8"/></svg>
        www.harbourlantern.com.au
      </span>
    </footer>
  </main>
</body>
</html>
```